Start-up needs a Web Design

We need a web design for a new Cleantech start-up based in California called "Ferrovane".

Background info on our company:

Our company is active in the area of wastewater treatment. We have a patent-pending treatment system to clean the wastewater that is collected by vacuum trucks from septic tanks. The cleaned water can be re-used.

Our clients can save up to 90% of the wastewater discharge fees by using our system instead of just dumping it.

The two founders of the company have successfully launched other Cleantech and Medtech startups before.

We are offering our services in the United States, Canada, Mexico, and the whole of Southern America.
Updates

Dear Designers for Ferrovane,

I have just updated the brief for the website of Ferrovane.

The main change to the brief is that the main graphic / photo of the website should not be "How it works", but a photo of Truck / containter.

All the best, Martin

Target Market(s)

n.a.

Industry/Entity Type

It Company

Requirements
Must have
• non
Nice to have
• non
Should not have
• n.a.

```html
<!DOCTYPE html>
<html lang="en">
<head>
<meta charset="utf-8">
<title>Ferrovane – Wastewater Treatment</title>
<link href="https://fonts.googleapis.com/css2?family=Arimo:wght@400;700&display=swap" rel="stylesheet">
<style>
:root{
  --slate:#4a5565;
  --slate-dark:#3c4654;
  --white:#ffffff;
  --orange:#f26a10;
  --steel-dark:#6f8995;
  --green:#6fa524;
  --ink:#1a1a1a;
  --text:#6b6b6b;
  --nav:#555555;
  --bullet:#1b3fc0;
  --brand:#1f4fb8;
  --hero-top:#8aa6c4;
  --hero-bottom:#6a7f52;
}
*{margin:0;padding:0;box-sizing:border-box}
html,body{width:1061px;height:1200px;overflow:hidden}
body{position:relative;background:var(--slate);font-family:"Arimo",Arial,sans-serif;color:var(--text)}
.abs{position:absolute}
.header-bg{position:absolute;left:0;top:0;width:1061px;height:240px}
.search-field{left:612px;top:27px;width:257px;height:32px;background:var(--white);border:1px solid #c9c9c9;box-shadow:inset 0 1px 2px rgba(0,0,0,.12)}
.search-button{left:884px;top:27px;width:87px;height:32px;background:var(--orange);color:var(--white);font-weight:700;font-size:16px;border-radius:3px;display:flex;align-items:center;justify-content:center}
.brand{left:91px;top:64px;display:flex;align-items:center;gap:14px}
.brand-square{width:52px;height:52px;background:var(--brand)}
.brand-name{font-size:52px;font-weight:700;color:var(--ink);letter-spacing:-1px;line-height:1}
.main-nav{left:491px;top:94px;display:flex;font-size:17px;color:var(--nav)}
.main-nav span{display:flex;align-items:center;gap:4px}
.main-nav i{display:inline-block;width:11px;height:11px;background:#555;clip-path:polygon(25% 0,75% 0,100% 50%,75% 100%,25% 100%,0 50%)}
.main-nav .active i{background:var(--orange)}
.hero-photo{left:89px;top:200px;width:883px;height:453px;background:linear-gradient(180deg,var(--hero-top),var(--hero-bottom))}
.hero-headline{left:117px;top:543px;color:var(--white);font-weight:700;font-size:37px;line-height:46px;text-shadow:0 2px 4px rgba(0,0,0,.45)}
.hero-headline b{font-size:46px}
.steps{left:89px;top:653px;width:883px;height:150px}
.step-text{color:var(--white);font-weight:700;text-align:center;font-size:17px;line-height:20px}
.step-number{color:var(--white);font-weight:700;font-size:62px;line-height:1}
.content-panel{left:0;top:810px;width:1061px;height:345px}
.col-title{font-size:25px;font-weight:400;line-height:1;padding-bottom:3px;border-bottom:1px solid currentColor}
.about .col-title{color:var(--orange)}
.advantages .col-title{color:var(--steel-dark)}
.founders .col-title{color:var(--green)}
.col-body{font-size:14px;line-height:16.4px;margin-top:5px}
.col-body li{list-style:none;position:relative;padding-left:12px;margin-bottom:5px}
.col-body li::before{content:"";position:absolute;left:1px;top:6px;width:5px;height:5px;border-radius:50%;background:#888}
.about li::before{background:var(--bullet)}
.more-btn{width:87px;height:32px;color:var(--white);font-weight:700;font-size:16px;border-radius:4px;display:flex;align-items:center;justify-content:center}
.divider{width:1px;background:#bdbdbd}
.founder-photo{width:94px;height:96px;background:linear-gradient(160deg,#3a4250,#8a8c92)}
.founder-name{font-size:15px;font-weight:700;color:var(--ink);line-height:17px}
.founder-role{font-size:12px;font-weight:700;color:var(--ink);line-height:14px}
.founder-text{font-size:13.5px;line-height:16px;color:var(--text);hyphens:auto}
.founder-more{color:var(--green);font-weight:700;float:right}
.footer-copy{left:89px;top:1170px;color:var(--white);font-size:16px}
.footer-links{right:90px;top:1168px;color:var(--white);font-size:16px;display:flex;gap:12px}
</style>
</head>
<body>

<svg class="header-bg" viewBox="0 0 1061 240" aria-hidden="true">
  <defs>
    <linearGradient id="headerFill" x1="0" y1="0" x2="0" y2="1">
      <stop offset="0" stop-color="#ffffff"/><stop offset="1" stop-color="#ececec"/>
    </linearGradient>
  </defs>
  <path d="M0 0H1061V232Q530 185 0 232Z" fill="url(#headerFill)"/>
</svg>

<div class="abs search-field"></div>
<div class="abs search-button">SEARCH</div>

<div class="abs brand">
  <div class="brand-square"></div>
  <div class="brand-name">Ferrovane</div>
</div>

<nav class="abs main-nav">
  <span class="active" style="width:100px"><i></i>HOME</span>
  <span style="width:133px"><i></i>ABOUT US</span>
  <span style="width:152px"><i></i>OUR CLIENT</span>
  <span><i></i>CONTACT</span>
</nav>

<div class="abs hero-photo" role="img" aria-label="Photo of a red vacuum truck with tank on a green field under a blue sky"></div>
<div class="abs hero-headline">Save up to <b>90%</b> on your<br>wastewater discharge fees.</div>

<svg class="abs steps" viewBox="0 0 883 150" aria-hidden="true">
  <defs>
    <linearGradient id="gOrange" x1="0" y1="0" x2="0" y2="1"><stop offset="0" stop-color="#f9a81f"/><stop offset="1" stop-color="#f3700f"/></linearGradient>
    <linearGradient id="gSteel" x1="0" y1="0" x2="0" y2="1"><stop offset="0" stop-color="#9fb7c2"/><stop offset="1" stop-color="#7f98a4"/></linearGradient>
    <linearGradient id="gGreen" x1="0" y1="0" x2="0" y2="1"><stop offset="0" stop-color="#acd44c"/><stop offset="1" stop-color="#64991f"/></linearGradient>
  </defs>
  <path d="M590 0H883V150H590Q625 75 590 0Z" fill="url(#gGreen)"/>
  <path d="M302 0H598Q633 75 598 150H302Q337 75 302 0Z" fill="var(--slate-dark)"/>
  <path d="M310 0H585Q620 75 585 150H310Q345 75 310 0Z" fill="url(#gSteel)"/>
  <path d="M0 0H292Q327 75 292 150H0Z" fill="url(#gOrange)"/>
  <g fill="none" stroke="#fff" stroke-width="3" stroke-linecap="round">
    <circle cx="142" cy="45" r="18"/>
    <path d="M134 62V74H150V62M136 80H148"/>
    <path d="M142 10V18M116 20L122 26M168 20L162 26M106 42H114M170 42H178"/>
  </g>
  <g fill="#fff">
    <rect x="406" y="16" width="70" height="26" rx="12"/>
    <rect x="480" y="22" width="10" height="20"/>
    <path d="M492 14H510L520 28V42H492Z"/>
    <circle cx="420" cy="46" r="6"/><circle cx="440" cy="46" r="6"/><circle cx="505" cy="46" r="6"/>
  </g>
  <path d="M730 10L756 22V50L730 62L704 50V22Z" fill="#8c8c8c"/>
  <path d="M730 10L756 22L730 34L704 22Z" fill="#b4b4b4"/>
</svg>

<div class="abs step-text" style="left:127px;top:759px;font-size:32px;line-height:1">How it works?</div>
<div class="abs step-number" style="left:410px;top:733px">1.</div>
<div class="abs step-text" style="left:448px;top:728px;width:220px">Pick up and<br>transport the wastewater<br>by vacuum truck</div>
<div class="abs step-number" style="left:724px;top:733px">2.</div>
<div class="abs step-text" style="left:776px;top:730px;width:170px">Clean and re-use<br>the water<br>at your own site</div>

<svg class="abs content-panel" viewBox="0 0 1061 345" aria-hidden="true">
  <path d="M89 12Q89 6 95 6H966Q972 6 972 12V320Q530 362 89 320Z" fill="#fff"/>
</svg>

<section class="abs about" style="left:112px;top:834px;width:266px">
  <h2 class="col-title">About Us</h2>
  <div class="col-body">
    <p>Ferrovane enables waste collection companies to easily clean their dirty wastewater. By cleaning their wastewater with our system, our clients can save up to 90% on the money they usually spend for their wastewater if they dump it at a communal treatment plant.</p>
    <ul style="margin-top:18px"><li>We know how to operate and maintain our system with all kind of different wastewaters.</li></ul>
  </div>
</section>
<div class="abs more-btn" style="left:288px;top:1075px;background:var(--orange)">MORE</div>
<div class="abs divider" style="left:387px;top:826px;height:292px"></div>

<section class="abs advantages" style="left:403px;top:834px;width:266px">
  <h2 class="col-title">Advantages</h2>
  <ul class="col-body" style="margin-top:9px">
    <li>By using our patent-pending wastewater treatment system, our clients can achieve huge cost savings!</li>
    <li>The cleaned water is of very high quality and can be re-used without any problems.</li>
    <li>Our clients do not have to make a big investment and buy a treatment system! They can rent the system from us at very low monthly rates and achieve savings of up to 90%!</li>
  </ul>
</section>
<div class="abs more-btn" style="left:576px;top:1075px;background:var(--steel-dark)">MORE</div>
<div class="abs divider" style="left:675px;top:826px;height:292px"></div>

<section class="abs founders" style="left:680px;top:834px;width:269px">
  <h2 class="col-title">The Founders</h2>
</section>
<div class="abs founder-photo" style="left:685px;top:867px" role="img" aria-label="Portrait photo of Martin Voss"></div>
<div class="abs" style="left:785px;top:864px;width:180px">
  <div class="founder-name">Martin Voss,</div>
  <div class="founder-role">Chief Executive Officer</div>
  <div class="founder-text">studied Marketing and Management at the University of Varlen in Switzerland and received the postgraduate title... <span class="founder-more">&raquo; More</span></div>
</div>
<div class="abs divider" style="left:685px;top:993px;width:274px;height:1px"></div>
<div class="abs founder-photo" style="left:685px;top:1013px" role="img" aria-label="Portrait photo of Owen Halbrook"></div>
<div class="abs" style="left:785px;top:1011px;width:180px">
  <div class="founder-name" style="color:var(--green)">Owen Halbrook</div>
  <div class="founder-role" style="color:var(--green)">Chief Financial Officer</div>
  <div class="founder-text">has extensive experience as an entrepreneur and as CFO at large multinational corporations... <span class="founder-more">&raquo; More</span></div>
</div>

<div class="abs footer-copy">© 2011 Ferrovane</div>
<div class="abs footer-links"><span>Home</span><span>|</span><span>About Us</span><span>|</span><span>Our Clients</span><span>|</span><span>Contact</span></div>

</body>
</html>
```